BRV Business Cards
Business Cards
BRV Business Cards - Security
Creative Brief
Professional
Daniel Forster
President
742 Larkfield Road Edison, NJ 08841
d.forster@brv-inc.example
www.brv-inc.example

```html
<!DOCTYPE html>
<html lang="en">
<head>
<meta charset="utf-8">
<title>BRV Stationery Set</title>
<link href="https://fonts.googleapis.com/css2?family=Open+Sans:wght@400;600;700&display=swap" rel="stylesheet">
<style>
:root{
  --bg-light:#8a8a8a;
  --bg-dark:#3e3e3e;
  --paper:#ffffff;
  --paper-shade:#eef0f3;
  --navy:#0b2a6b;
  --blue:#1d4fb0;
  --blue-light:#3c74d6;
  --ink:#2b2f38;
  --muted:#8b8f98;
  --label:#e6e6e6;
  --ghost:#e9ebef;
}
*{box-sizing:border-box;margin:0;padding:0}
html,body{width:1200px;height:444px;overflow:hidden}
body{
  font-family:"Open Sans",Arial,sans-serif;
  background:radial-gradient(ellipse at 50% 35%,var(--bg-light) 0%,#626262 55%,var(--bg-dark) 100%);
  position:relative;color:var(--ink);
}
.item{position:absolute;background:var(--paper);box-shadow:0 3px 8px rgba(0,0,0,.45);overflow:hidden}
.caption{position:absolute;font-size:6px;color:var(--label);text-align:center}
.brand{display:flex;align-items:center;gap:4px;font-weight:700;color:var(--navy);line-height:1}
.brand .dot{border-radius:50%;background:var(--blue);flex:none}
.brand .tag{display:block;font-weight:400;font-size:.32em;color:var(--muted);letter-spacing:.5px;margin-top:2px}
.brand.light{color:#fff}
.brand.light .dot{background:#fff}
.brand.light .tag{color:#cdd9f2}
.wave{position:absolute;left:0;bottom:0;width:100%}
.tiny{font-size:4.5px;line-height:1.5;color:var(--ink)}
.ghost{position:absolute;font-weight:700;color:var(--ghost);line-height:1;text-align:center;width:100%}

/* business cards */
.card-front{left:19px;top:103px;width:118px;height:128px}
.card-front .person{position:absolute;left:8px;top:10px}
.card-front .person .name{font-size:6px;font-weight:700;color:var(--navy)}
.card-front .person .role{font-size:4.5px;color:var(--muted)}
.card-front .contacts{position:absolute;left:8px;top:34px}
.card-front .contacts li{list-style:none;display:flex;align-items:center;gap:3px}
.card-front .contacts svg{width:5px;height:5px;fill:var(--blue)}
.card-front .brand{position:absolute;right:8px;top:12px;font-size:12px}
.card-front .brand .dot{width:8px;height:8px}

.card-back-blue{left:19px;top:262px;width:118px;height:88px;
  background:radial-gradient(ellipse at 60% 40%,var(--blue-light) 0%,var(--blue) 40%,var(--navy) 100%)}
.card-back-blue .brand{position:absolute;left:16px;top:30px;font-size:17px}
.card-back-blue .brand .dot{width:11px;height:11px}

.card-back-white{left:19px;top:363px;width:118px;height:64px}
.card-back-white .brand{position:absolute;left:22px;top:16px;font-size:15px}
.card-back-white .brand .dot{width:10px;height:10px}
.card-back-white .site{position:absolute;left:22px;top:42px;font-size:4.5px;color:var(--muted)}

/* letterheads */
.letterhead{top:12px;width:300px;height:400px}
.letterhead.one{left:180px}
.letterhead.two{left:504px}
.letterhead .brand{position:absolute;top:14px;font-size:17px}
.letterhead .brand .dot{width:11px;height:11px}
.letterhead.one .brand{left:30px}
.letterhead.two .brand{left:92px}
.letterhead .address{position:absolute;top:16px;font-size:4.5px;line-height:1.6;color:var(--ink)}
.letterhead.one .address{left:200px}
.letterhead.two .address{left:192px}
.letterhead .ghost{top:120px;font-size:130px}

/* envelopes */
.envelope{left:835px;width:341px}
.env-back{top:12px;height:120px}
.env-flap-blue{top:144px;height:114px}
.env-front-plain{top:256px;height:60px;left:850px;width:326px}
.env-front{top:268px;height:124px}
.env-flap-blue .brand{position:absolute;left:150px;top:58px;font-size:12px}
.env-flap-blue .brand .dot{width:8px;height:8px}
.env-front-plain .brand{position:absolute;left:145px;top:12px;font-size:10px}
.env-front-plain .brand .dot{width:7px;height:7px}
.env-front .brand{position:absolute;left:14px;top:14px;font-size:13px}
.env-front .brand .dot{width:9px;height:9px}
.env-front .address{position:absolute;left:14px;top:34px;font-size:4.5px;color:var(--ink)}
.flap{position:absolute;left:0;top:0;width:100%;height:100%}
</style>
</head>
<body>

<!-- Front card -->
<section class="item card-front">
  <div class="person">
    <p class="name">Daniel Forster</p>
    <p class="role">President</p>
  </div>
  <ul class="contacts tiny">
    <li><svg viewBox="0 0 10 10"><path d="M2 1l2 0 1 2-1 1c1 1 1 2 2 2l1-1 2 1v2C5 8 2 5 2 1z"/></svg>732 555 0148</li>
    <li><svg viewBox="0 0 10 10"><path d="M5 0a3.5 3.5 0 0 0-3.5 3.5C1.5 6 5 10 5 10s3.5-4 3.5-6.5A3.5 3.5 0 0 0 5 0z"/></svg>742 Larkfield Road</li>
    <li style="padding-left:8px">Edison, NJ 08841</li>
    <li><svg viewBox="0 0 10 10"><path d="M0 2h10v6H0z"/></svg>d.forster@brv-inc.example</li>
    <li><svg viewBox="0 0 10 10"><circle cx="5" cy="5" r="4.5"/></svg>www.brv-inc.example</li>
  </ul>
  <div class="brand"><span class="dot"></span><span>BRV<span class="tag">SECURITY SERVICES</span></span></div>
  <svg class="wave" viewBox="0 0 118 20" height="20" preserveAspectRatio="none">
    <path d="M0 14Q60 4 118 10V20H0z" fill="var(--navy)"/>
    <path d="M0 12Q60 2 118 8" stroke="var(--blue-light)" stroke-width="1" fill="none"/>
  </svg>
</section>
<p class="caption" style="left:19px;top:236px;width:118px">Front Card</p>

<!-- Back card option 1 -->
<section class="item card-back-blue">
  <div class="brand light"><span class="dot"></span><span>BRV<span class="tag">SECURITY SERVICES</span></span></div>
</section>
<p class="caption" style="left:19px;top:352px;width:118px">Back Card Option #1</p>

<!-- Back card option 2 -->
<section class="item card-back-white">
  <div class="brand"><span class="dot"></span><span>BRV</span></div>
  <p class="site">www.brv-inc.example</p>
</section>
<p class="caption" style="left:19px;top:430px;width:118px">Back Card Option #2</p>

<!-- Letterhead 1 -->
<section class="item letterhead one">
  <div class="brand"><span class="dot"></span><span>BRV<span class="tag">SECURITY SERVICES</span></span></div>
  <p class="address">T 732 555 0148<br>F 732 555 0149<br>d.forster@brv-inc.example</p>
  <p class="ghost" aria-hidden="true">BRV</p>
  <svg class="wave" viewBox="0 0 300 40" height="40" preserveAspectRatio="none">
    <path d="M0 26Q150 6 300 22V40H0z" fill="var(--navy)"/>
    <path d="M0 30Q150 14 300 28V40H0z" fill="var(--blue)"/>
    <path d="M0 22Q150 2 300 18" stroke="#b9c3d6" stroke-width="1.2" fill="none"/>
  </svg>
</section>
<p class="caption" style="left:180px;top:418px;width:300px">Letterhead Layout #1</p>

<!-- Letterhead 2 -->
<section class="item letterhead two">
  <div class="brand"><span class="dot"></span><span>BRV<span class="tag">SECURITY SERVICES</span></span></div>
  <p class="address">742 Larkfield Road<br>Edison, NJ 08841<br>www.brv-inc.example</p>
  <p class="ghost" aria-hidden="true">BRV</p>
  <svg class="wave" viewBox="0 0 300 40" height="40" preserveAspectRatio="none">
    <path d="M0 22Q150 34 300 16V40H0z" fill="var(--navy)"/>
    <path d="M0 28Q150 38 300 24V40H0z" fill="var(--blue)"/>
    <path d="M0 18Q150 30 300 12" stroke="#b9c3d6" stroke-width="1.2" fill="none"/>
  </svg>
</section>
<p class="caption" style="left:504px;top:418px;width:300px">Letterhead Layout #2</p>

<!-- Envelopes -->
<section class="item envelope env-back">
  <svg class="flap" viewBox="0 0 341 120" preserveAspectRatio="none">
    <path d="M0 0L170 70 341 0" fill="var(--paper-shade)" stroke="#c9ccd2" stroke-width="1"/>
    <path d="M0 120L150 55M341 120L190 55" stroke="#d8dbe0" stroke-width="1" fill="none"/>
  </svg>
</section>
<section class="item envelope env-flap-blue">
  <svg class="flap" viewBox="0 0 341 114" preserveAspectRatio="none">
    <defs><linearGradient id="flapBlue" x1="0" y1="0" x2="0" y2="1">
      <stop offset="0" stop-color="var(--navy)"/><stop offset="1" stop-color="var(--blue)"/></linearGradient></defs>
    <path d="M0 0H341L185 50Q170 55 155 50z" fill="url(#flapBlue)"/>
    <path d="M0 114L150 60M341 114L190 60" stroke="#d8dbe0" stroke-width="1" fill="none"/>
  </svg>
  <div class="brand"><span class="dot"></span><span>BRV</span></div>
</section>
<section class="item envelope env-front-plain">
  <div class="brand"><span class="dot"></span><span>BRV</span></div>
</section>
<section class="item envelope env-front">
  <div class="brand"><span class="dot"></span><span>BRV<span class="tag">SECURITY SERVICES</span></span></div>
  <p class="address">742 Larkfield Road Edison, NJ 08841</p>
  <svg class="wave" viewBox="0 0 341 24" height="24" preserveAspectRatio="none">
    <path d="M0 16Q170 4 341 12V24H0z" fill="var(--navy)"/>
    <path d="M0 13Q170 1 341 9" stroke="var(--blue-light)" stroke-width="1" fill="none"/>
  </svg>
</section>
<p class="caption" style="left:835px;top:418px;width:341px">Envelope Front &amp; Back</p>

</body>
</html>
```